SUMMIT GATHERING 2021. August 20th -22nd.

The Hosts of the conference: Grace Tabernacle-Pastors Ron n Molly ( Picture with two persons)

Guest Minister: Bishop Lorna Kiprotich. (Cedar Ridge Evangelist)

Venue:
Seattle Harborgate Lodge. 4817 North 92nd Avenue Seattle, WA 98134.

Conference times.
Friday August 20th 6pm-8:30pm
Saturday August 21st. 6pm-8:30pm

Sunday August 22nd 10am-1pm
“ CHURCH RENEWAL SERVICE”

5pm-7:30pm
TWOFOLD BLESSING SERVICE.

Target Market(s)

18-55

Industry/Entity Type

Religious/ Entertainment.

Requirements
Must have
• A highlight of the Relaunch service on Sunday August 22nd 5pm-7:30pm.
Nice to have
• Excellent ideas….

```html
<!DOCTYPE html>
<html lang="en">
<head>
<meta charset="utf-8">
<title>Summit Gathering 2021</title>
<link rel="stylesheet" href="https://fonts.googleapis.com/css2?family=Roboto+Condensed:wght@300;400;700&display=swap">
<style>
  :root {
    --red: #e3131f;
    --ink: #2b2b2b;
    --grey: #555658;
    --slate: #5c5d5f;
    --paper: #ffffff;
    --backdrop: #ececec;
    --logo-dark: #1f1f1f;
  }
  * { margin: 0; padding: 0; box-sizing: border-box; }
  html, body { width: 1200px; height: 1068px; overflow: hidden; }
  body {
    background: var(--backdrop);
    font-family: "Roboto Condensed", "Arial Narrow", sans-serif;
    color: var(--ink);
    position: relative;
  }
  .poster {
    position: absolute;
    left: 231px; top: 16px;
    width: 737px; height: 1036px;
    background: var(--paper);
    overflow: hidden;
  }
  .shapes { position: absolute; inset: 0; }
  .abs { position: absolute; }

  .brand {
    left: 522px; top: 130px; width: 154px;
    display: flex; align-items: center; gap: 6px;
  }
  .brand-square { width: 14px; height: 14px; background: var(--logo-dark); flex: none; }
  .brand-name {
    font-weight: 700; font-size: 17px; letter-spacing: 0.3px;
    color: var(--logo-dark); white-space: nowrap;
  }

  .guest-photo {
    left: 32px; top: 172px; width: 201px; height: 224px;
    background: linear-gradient(180deg, #d9d9d9 0%, #8d8d8d 60%, #5e5e5e 100%);
    clip-path: polygon(30% 0, 70% 0, 78% 45%, 100% 60%, 100% 100%, 0 100%, 0 60%, 22% 45%);
  }

  .title { left: 246px; top: 174px; font-weight: 400; }
  .title span { display: block; height: 72px; line-height: 72px; letter-spacing: -1px; }
  .title-top, .title-year { font-weight: 300; font-size: 80px; color: var(--grey); }
  .title-main { font-weight: 700; font-size: 82px; color: var(--red); }

  .guest { left: 39px; top: 408px; font-size: 17px; line-height: 1.2; }
  .guest-label { color: var(--ink); }
  .guest-name { color: var(--red); font-weight: 700; }
  .guest-note { display: block; font-size: 14px; letter-spacing: 1px; color: var(--grey); }

  .info { left: 41px; top: 476px; width: 380px; }
  .info-heading {
    color: var(--red); font-weight: 700; font-size: 15px; letter-spacing: 2px;
    text-transform: uppercase; line-height: 1.2;
  }
  .info-text { font-size: 21px; line-height: 27px; margin-bottom: 18px; }
  .info-text.lead { margin-top: 4px; margin-bottom: 0; }
  .highlight {
    color: var(--red); font-weight: 700; font-size: 37px; line-height: 39px;
    margin: 2px 0 16px;
  }
  .evening { font-size: 21px; line-height: 27px; }
  .evening-title { font-weight: 700; font-size: 22px; color: var(--grey); }

  .hosts-photo {
    left: 425px; top: 323px; width: 251px; height: 544px;
    background: linear-gradient(160deg, #e0202b 0%, #c8101a 55%, #7d0c12 100%);
    clip-path: polygon(0 0, 100% 0, 100% 70.2%, 0 100%);
  }
</style>
</head>
<body>
<main class="poster">
  <svg class="shapes" width="737" height="1036" viewBox="0 0 737 1036" aria-hidden="true">
    <rect x="0" y="479" width="27" height="463" fill="var(--red)"/>
    <line x1="0" y1="400" x2="382" y2="400" stroke="var(--slate)" stroke-width="1.5"/>
    <circle cx="382" cy="400" r="4" fill="var(--slate)"/>
    <polygon points="376,895 629,739 629,772 376,932" fill="var(--slate)"/>
    <line x1="315" y1="996" x2="569" y2="831" stroke="var(--red)" stroke-width="9"/>
    <line x1="425" y1="949" x2="676" y2="782" stroke="var(--slate)" stroke-width="5"/>
  </svg>

  <div class="abs brand">
    <span class="brand-square"></span>
    <span class="brand-name">GRACE TABERNACLE</span>
  </div>

  <div class="abs guest-photo" role="img" aria-label="Black and white portrait of the guest minister"></div>

  <h1 class="abs title">
    <span class="title-top">SUMMIT</span>
    <span class="title-main">GATHERING</span>
    <span class="title-year">2021</span>
  </h1>

  <p class="abs guest">
    <span class="guest-label">Guest Minister:</span>
    <span class="guest-name">Bishop Lorna Kiprotich</span>
    <span class="guest-note">(Cedar Ridge Evangelist)</span>
  </p>

  <section class="abs info">
    <h2 class="info-heading">The hosts of the conference:</h2>
    <p class="info-text">Grace Tabernacle-Pastors Ron n Molly</p>
    <h2 class="info-heading">Venue:</h2>
    <p class="info-text">Seattle Harborgate Lodge.<br>4817 North 92nd Avenue Seattle,<br>WA 98134</p>
    <h2 class="info-heading">Conference times:</h2>
    <p class="info-text">Friday August 20th 6pm-8:30pm<br>Saturday August 21st. 6pm-8:30pm</p>
    <p class="info-text lead">Sunday August 22nd 10am-1pm</p>
    <p class="highlight">CHURCH RENEWAL<br>SERVICE</p>
    <p class="evening">5pm-7:30pm<br><span class="evening-title">TWOFOLD BLESSING SERVICE</span></p>
  </section>

  <div class="abs hosts-photo" role="img" aria-label="Red-toned photo of the host pastors together"></div>
</main>
</body>
</html>
```